Personalised WINE LABLE
personalised bordeaux bottle
Hi!
I have sent you a private message, please feedback.
Thanks!!!
Ok, a few more changes:
The back drop of the Palace cannot look like a mosque (esp. the one in istanbul)- the back drop palace form number 9 was the best- please use this..
The face needs to be more resembling of DON VELMARIZO but with with those same traits- moustache, beard, nose etc.
Font- other then CHATEAU DON VELMARIZO- more Arab looking!
Almost there, the rest is great!!
Wine bottle or a classic genie bottle / lamp?
ALmost there! Please make the genie coming out of a bottle!
Sounds good, I'll try to make a couple more versions in a couple of days. It's FUN to work on this project, thanks for the opportunity :)
PMARVIN: A little more friendly, similar Genie but with a big belly and winking one eye, with a slight smirk on his face. Please try to imitate Prince Tavrek's face from lookwell images (but without the glasses)!
http://www.lookwell-example.co.uk/imgres?q=PRINCE+TAVREK+BAHRAIN&imgrefurl=http://newsquill-example.com/International/royal-wedding-prince-tavrek-bahrain-declines-invitation/story%3Fid%3D10000001&imgurl=http://img.newsquill-example.com/images/International/Prince_Tavrek_Bin_Odell_al_Varnesh_Bahrain.jpg
who is Don Velmarizo? Send me a fiew informations about him. Is he from Asia, Africa or Spain???
Hi,
Here are the answers!
- Do you want any additional lines of text on the label (like year, type of vine, region, etc.)?
Great! Year: 2012 --- Region: Bordeaux
- Do you have any color preferences?
No Colour preferences
- As for the bottle title, do you want it to read "DON VELMARIZO" or "CHATEAUX DON VELMARIZO"?
CHATEAUX DON VELMARIZO
Thanks
Hello. It looks like a very interesting project, I have started working on it. So far I have a few questions:
Thank you
http://www.keepsakemarket-example.com/french-placemats/bordeaux-wine-label-placemats-set-of--100.html
HERE IS A GOOD EXAMPLE TO START FROM
SIMILAR - USING THE BRIEF DESCRIPTION WITH THE TITLES BELOW
TITLE: CHATEAUX DON VELMARIZO
SUBTITLE: MIS EN BOUTEILLE AUX PALAIS

```html
<!DOCTYPE html>
<html lang="fr">
<head>
<meta charset="utf-8">
<title>Chateaux Don Velmarizo – Wine Label</title>
<link rel="stylesheet" href="https://fonts.googleapis.com/css2?family=Old+Standard+TT:wght@400;700&family=Playfair+Display:wght@900&display=swap">
<style>
  :root {
    --canvas: #ffffff;
    --paper: #f3ead8;
    --wine: #8c2333;
    --wine-soft: #a9434f;
    --ink: #4a2a24;
  }
  * { box-sizing: border-box; margin: 0; padding: 0; }
  html, body { width: 1200px; height: 799px; overflow: hidden; background: var(--canvas); }
  .stage { position: relative; width: 1200px; height: 799px; }

  .label {
    position: absolute; left: 100px; top: 111px;
    width: 1000px; height: 576px;
    background: var(--paper);
    border: 6px solid var(--wine);
    color: var(--wine);
    font-family: "Old Standard TT", "Times New Roman", serif;
    text-align: center;
  }
  .label__inner-rule {
    position: absolute; inset: 12px;
    border: 2px solid var(--wine);
  }
  .label p, .label h1 {
    position: absolute; left: 0; right: 0;
    line-height: 1; white-space: nowrap;
  }

  .grapes {
    position: absolute; top: 28px; width: 90px; height: 122px;
  }
  .grapes--left { left: 28px; }
  .grapes--right { right: 28px; }

  .vintage {
    top: 34px;
    font-size: 28px; font-weight: 700; letter-spacing: 1px;
  }
  .appellation {
    top: 66px;
    font-size: 32px; font-weight: 700; letter-spacing: 0.5px;
  }

  .palace-scene {
    position: absolute; left: 150px; top: 108px;
    width: 700px; height: 186px;
  }

  .chateau-name {
    top: 300px;
    font-family: "Playfair Display", Georgia, serif;
    font-weight: 900; font-size: 56px; letter-spacing: -1px;
  }
  .classification {
    top: 364px;
    font-size: 18px; font-weight: 700; letter-spacing: 3px;
  }
  .region {
    top: 390px;
    font-size: 44px; font-weight: 700; letter-spacing: 1px;
  }
  .bottling {
    top: 442px;
    font-size: 26px; letter-spacing: 0.5px;
  }
  .producer {
    top: 480px;
    font-size: 16px; line-height: 22px !important; color: var(--ink);
  }
</style>
</head>
<body>
<div class="stage">
  <section class="label">
    <div class="label__inner-rule"></div>

    <svg class="grapes grapes--left" role="img" aria-label="Grape cluster with vine leaves ornament" viewBox="0 0 90 122">
      <rect width="90" height="122" rx="28" fill="var(--wine-soft)" opacity="0.85"/>
    </svg>
    <svg class="grapes grapes--right" role="img" aria-label="Grape cluster with vine leaves ornament" viewBox="0 0 90 122">
      <rect width="90" height="122" rx="28" fill="var(--wine-soft)" opacity="0.85"/>
    </svg>

    <p class="vintage">2012</p>
    <p class="appellation">APPELLATION MARGAUX CONTROLEE</p>

    <svg class="palace-scene" role="img" aria-label="Illustration of a smiling genie rising above a domed Arabian palace silhouette, with camels, dancers and palm trees" viewBox="0 0 700 186">
      <defs>
        <linearGradient id="sceneTone" x1="0" y1="0" x2="0" y2="1">
          <stop offset="0" stop-color="#c9a9a0"/>
          <stop offset="0.45" stop-color="#a9434f"/>
          <stop offset="1" stop-color="#8c2333"/>
        </linearGradient>
      </defs>
      <rect x="0" y="0" width="700" height="186" rx="6" fill="url(#sceneTone)"/>
    </svg>

    <h1 class="chateau-name">CHATEAUX DON VELMARIZO</h1>
    <p class="classification">CRU BOURGEOIS</p>
    <p class="region">MARGAUX</p>
    <p class="bottling">MIS EN BOUTEILLE AUX PALAIS</p>
    <p class="producer">G.F.A. LA TOUR DE VERNAC - Propriatalia<br>Verlac- en - Medoc 33475 Margaux</p>
  </section>
</div>
</body>
</html>
```